Business Card Design

We need a business card design for a consulting firm which provides safety and risk management consulting services for public venues, hotels and tourist attractions. The business card design should include the attached logo unedited with a design based on incorporating the existing logo with a design of geometric patterns or lines on a predominantly white background.

Industry/Entity Type

Business

Contact Information for Business Card

Dane Morravik
Director & Principal Consultant

Ph: +61 (0) 478506 214
PO Box 456 Brenmoor Vale, NSW Australia 2611
info@corvalrisksafety.example

(back of card to include website www.corvalrisksafety.example

```html
<!DOCTYPE html>
<html lang="en">
<head>
<meta charset="utf-8">
<title>Corval Risk &amp; Safety – Business Card</title>
<link href="https://fonts.googleapis.com/css2?family=Open+Sans:wght@400;600&display=swap" rel="stylesheet">
<style>
  :root {
    --brand-blue: #1a8fd0;
    --brand-green: #3cbf3a;
    --card-white: #ffffff;
    --backdrop: #e6e7e9;
    --ink-white: #ffffff;
  }
  * { box-sizing: border-box; margin: 0; padding: 0; }
  html, body {
    width: 1200px; height: 873px; overflow: hidden;
    background: var(--backdrop);
    font-family: "Open Sans", Arial, sans-serif;
  }
  .sheet {
    width: 1200px; height: 873px;
    display: flex; align-items: center; justify-content: center; gap: 40px;
  }
  .card {
    position: relative; width: 540px; height: 309px;
    background: var(--card-white);
    box-shadow: 0 6px 18px rgba(0,0,0,0.15);
    overflow: hidden;
  }
  .card__top-strip {
    position: absolute; top: 0; left: 0; right: 0; height: 10px;
    background: var(--brand-blue);
  }
  .card__band {
    position: absolute; left: 0; right: 0; bottom: 0;
    background: var(--brand-blue);
    color: var(--ink-white);
    display: flex; align-items: center;
  }
  /* front */
  .card--front .card__band {
    height: 82px; border-top: 5px solid var(--brand-green);
    justify-content: space-between; padding: 0 34px;
    font-size: 13px;
  }
  .contact-line { display: flex; align-items: center; gap: 8px; }
  .contact-line svg { flex: none; }
  .person { position: absolute; left: 38px; top: 38px; }
  .person__name {
    color: var(--brand-blue); font-weight: 600; font-size: 30px; line-height: 1.1;
  }
  .person__role {
    color: var(--brand-green); font-size: 14px; margin-top: 4px;
  }
  .person__address {
    display: flex; gap: 8px; margin-top: 16px;
    color: var(--brand-green); font-size: 13px; line-height: 1.45;
  }
  .person__address svg { margin-top: 2px; flex: none; }
  .brand-mark {
    position: absolute; right: 34px; top: 110px;
    display: flex; align-items: center; gap: 10px;
    color: var(--brand-blue); font-weight: 600; font-size: 18px;
  }
  .brand-mark__dot {
    width: 14px; height: 14px; border-radius: 50%; background: var(--brand-green);
  }
  /* back */
  .card--back .card__band {
    height: 64px; padding: 0 34px; font-size: 14px; letter-spacing: 0.3px;
  }
  .card--back .brand-mark {
    right: auto; left: 0; width: 100%; top: 100px;
    justify-content: center; font-size: 34px; gap: 14px;
  }
  .card--back .brand-mark__dot { width: 22px; height: 22px; }
</style>
</head>
<body>
<main class="sheet">
  <section class="card card--front" aria-label="Business card front">
    <div class="card__top-strip"></div>
    <div class="person">
      <h1 class="person__name">Dane Morravik</h1>
      <p class="person__role">Director &amp; Principal Consultant</p>
      <div class="person__address">
        <svg width="11" height="14" viewBox="0 0 11 14" aria-hidden="true"><path d="M5.5 0A5.5 5.5 0 0 0 0 5.5C0 9.5 5.5 14 5.5 14S11 9.5 11 5.5A5.5 5.5 0 0 0 5.5 0zm0 7.6a2.1 2.1 0 1 1 0-4.2 2.1 2.1 0 0 1 0 4.2z" fill="#3cbf3a"/></svg>
        <p>PO Box 456 Brenmoor Vale,<br>NSW Australia 2611</p>
      </div>
    </div>
    <div class="brand-mark"><span class="brand-mark__dot"></span><span>Corval Risk &amp; Safety</span></div>
    <div class="card__band">
      <p class="contact-line">
        <svg width="13" height="13" viewBox="0 0 13 13" aria-hidden="true"><rect x="1" y="4" width="11" height="8" rx="1.5" fill="#fff"/><path d="M2 4.5C2 1.5 11 1.5 11 4.5" stroke="#fff" stroke-width="2" fill="none"/></svg>
        +61 (0) 478506 214
      </p>
      <p class="contact-line">
        <svg width="14" height="10" viewBox="0 0 14 10" aria-hidden="true"><rect x="0.5" y="0.5" width="13" height="9" fill="none" stroke="#fff"/><path d="M0.5 0.5L7 6l6.5-5.5" fill="none" stroke="#fff"/></svg>
        info@corvalrisksafety.example
      </p>
    </div>
  </section>

  <section class="card card--back" aria-label="Business card back">
    <div class="card__top-strip"></div>
    <div class="brand-mark"><span class="brand-mark__dot"></span><span>Corval Risk &amp; Safety</span></div>
    <div class="card__band">
      <p>www.corvalrisksafety.example</p>
    </div>
  </section>
</main>
</body>
</html>
```